Travelogue book cover

The book is a collection of stories from my travels around the world. These stories run a full range of emotions from unbridled joy, to things that are much funnier today than they were at the time, to moments of sadness while reflecting on places that have been irrevocably changed. This world is an amazing and powerful place, and my stories tell its tale. The overall vibe is to love exploring the world, the thrill of discovery, the comedy of getting outside of your comfort zone, and just generally wanting to convey a sense of wonder and make people feel like they want to get out and explore for themselves.

The audience is in the 30-50 age target, educated, all genders, and either an experienced traveller or wishes they were.

On the style, I am looking for something that stands out when a reader is browsing Brellowmart. Since most book covers are bright, full bleed and busy, I would prefer something that emphasizes white space and simplicity.

```html
<!DOCTYPE html>
<html lang="en">
<head>
<meta charset="utf-8">
<title>Travelogue – Book Cover</title>
<link rel="stylesheet" href="https://fonts.googleapis.com/css2?family=Bebas+Neue&family=Montserrat:wght@400;500&display=swap">
<style>
  :root {
    --backdrop: #d4d4d4;
    --cover-white: #ffffff;
    --cover-shade: #ececec;
    --orange: #f7901e;
    --orange-deep: #e07a0a;
    --tagline-grey: #555555;
    --author-white: #f4f4f4;
    --hue-red: #e8331c;
    --hue-orange: #f58220;
    --hue-yellow: #e4dd14;
    --hue-green: #12a85a;
    --hue-cyan: #1fa0dc;
    --hue-blue: #4a5fd6;
    --hue-purple: #9b4fd8;
    --hue-magenta: #e0157a;
  }

  * { margin: 0; padding: 0; box-sizing: border-box; }

  html, body {
    width: 1200px;
    height: 1200px;
    overflow: hidden;
    background: var(--backdrop);
  }

  .canvas {
    position: relative;
    width: 1200px;
    height: 1200px;
  }

  .book-cover {
    position: absolute;
    left: 233px;
    top: 50px;
    width: 734px;
    height: 1100px;
    background: linear-gradient(90deg, var(--cover-white) 0%, var(--cover-shade) 55%, var(--cover-white) 100%);
    overflow: hidden;
  }

  .cover-title {
    position: absolute;
    top: 66px;
    left: 0;
    width: 100%;
    text-align: center;
    font-family: "Bebas Neue", sans-serif;
    font-size: 170px;
    line-height: 1;
    letter-spacing: 0.005em;
    background: linear-gradient(90deg, var(--orange) 0%, var(--orange-deep) 50%, var(--orange) 100%);
    -webkit-background-clip: text;
    background-clip: text;
    color: transparent;
  }

  .journey-ring {
    position: absolute;
    left: 93px;
    top: 353px;
    width: 640px;
    height: 640px;
    border-radius: 50%;
    background: conic-gradient(
      var(--hue-red) 0deg,
      var(--hue-orange) 60deg,
      var(--hue-yellow) 110deg,
      var(--hue-green) 145deg,
      var(--hue-cyan) 185deg,
      var(--hue-blue) 230deg,
      var(--hue-purple) 290deg,
      var(--hue-magenta) 330deg,
      var(--hue-red) 360deg
    );
    opacity: 0.85;
  }

  .ring-centre {
    position: absolute;
    left: 245px;
    top: 505px;
    width: 336px;
    height: 336px;
    border-radius: 50%;
    background: var(--cover-shade);
    display: flex;
    align-items: center;
    justify-content: center;
  }

  .tagline {
    font-family: "Montserrat", sans-serif;
    font-weight: 400;
    font-size: 24px;
    line-height: 35px;
    color: var(--tagline-grey);
    text-align: center;
    width: 230px;
  }

  .author-band {
    position: absolute;
    left: 0;
    bottom: 0;
    width: 100%;
    height: 69px;
    background: linear-gradient(90deg, var(--orange) 0%, var(--orange-deep) 50%, var(--orange) 100%);
    display: flex;
    align-items: center;
    justify-content: center;
  }

  .author-name {
    font-family: "Montserrat", sans-serif;
    font-weight: 500;
    font-size: 36px;
    letter-spacing: 0.12em;
    color: var(--author-white);
    padding-left: 0.12em;
  }
</style>
</head>
<body>
  <main class="canvas">
    <section class="book-cover">
      <h1 class="cover-title">Travelogue</h1>
      <div class="journey-ring" role="img" aria-label="Rainbow-coloured line illustration of world landmarks, a hot-air balloon, a ship, a plane and palm trees arranged around a small globe"></div>
      <div class="ring-centre">
        <p class="tagline">This world is an amazing and powerful place, and my stories tell its tale</p>
      </div>
      <footer class="author-band">
        <span class="author-name">AUTHOR NAME</span>
      </footer>
    </section>
  </main>
</body>
</html>
```